Social Media Graphics - ALL TEXT RK

We are looking for a series of social media graphics for Instagram (standard size 1:1 (1080x1080px) that are ALL TEXT. We want the following quotes below on each graphic; one quote per graphic. AND, In very small letters at the bottom of each graphic, add @RKMarlowLive

The look and feel of these graphics should be complimentary to the color palette attached below; but keep them simple. But the design is up to you; at the end of this document, I provided various samples of all text graphics that I like as examples.

Target Market(s)

women looking to lose weight

Industry/Entity Type

health and wellness

Colors
E54698
E96AAD
F1A4CE
F9D9EA
FCEFF6

Requirements
Must have
• the quotes in the document
Should not have
• no stock photography

```html
<!DOCTYPE html>
<html lang="en">
<head>
<meta charset="utf-8">
<title>RK Social Quote Series</title>
<link rel="stylesheet" href="https://fonts.googleapis.com/css2?family=Prata&display=swap">
<style>
  :root {
    --ink: #d9267e;
    --mark: #f9cde3;
    --quote-mark: #efc3cf;
    --frame: #3a3a3a;
    --paper: #ffffff;
  }
  * { margin: 0; padding: 0; box-sizing: border-box; }
  html, body {
    width: 1200px; height: 509px; overflow: hidden;
    background: var(--paper);
  }
  .series { position: relative; width: 1200px; height: 509px; }
  .quote-card {
    position: absolute;
    width: 177px; height: 177px;
    border: 1px solid var(--frame);
    background: var(--paper);
    display: flex; align-items: center; justify-content: center;
    padding: 0 8px 10px;
  }
  .quote-card::before {
    content: "\201D";
    position: absolute; left: 9px; top: -2px;
    font-family: "Prata", serif;
    font-size: 30px; line-height: 1;
    color: var(--quote-mark);
  }
  .quote-text {
    font-family: "Prata", serif;
    font-size: 14.2px; line-height: 18px;
    color: var(--ink);
    text-align: center;
    white-space: nowrap;
  }
  .hl {
    background: var(--mark);
    padding: 0 4px;
    border-radius: 1px;
  }
  .handle {
    position: absolute; left: 0; right: 0; bottom: 11px;
    font-family: "Prata", serif;
    font-size: 3.6px; letter-spacing: 0.1px;
    text-transform: uppercase;
    color: var(--ink);
    text-align: center;
  }
  .col-1 { left: 68px; } .col-2 { left: 294px; } .col-3 { left: 520px; }
  .col-4 { left: 742px; } .col-5 { left: 960px; }
  .row-1 { top: 60px; } .row-2 { top: 277px; }
</style>
</head>
<body>
<main class="series">
  <article class="quote-card col-1 row-1">
    <p class="quote-text">Wake up<br>tomorrow with a<br><span class="hl">flatter belly</span><br>- yes,<br>this overnight<br>remedy works<br><span class="hl">&nbsp;like magic!&nbsp;</span></p>
    <p class="handle">@RKMarlowLive</p>
  </article>
  <article class="quote-card col-2 row-1">
    <p class="quote-text">Struggling with<br>bloating and<br><span class="hl">belly fat?</span> Try<br>this natural<br>solution tonight,<br>and wake up<br><span class="hl">feeling lighter!</span></p>
    <p class="handle">@RKMarlowLive</p>
  </article>
  <article class="quote-card col-3 row-1">
    <p class="quote-text">One<br>supplement,<br>one night; your<br><span class="hl">belly bloat</span> could<br>be gone by<br>morning. Here's<br><span class="hl">how it works!</span></p>
    <p class="handle">@RKMarlowLive</p>
  </article>
  <article class="quote-card col-4 row-1">
    <p class="quote-text"><span class="hl">Finally-a</span><br>natural<br>solution that<br>flattens your<br>belly AND<br>eases<br><span class="hl">stomach bloat</span></p>
    <p class="handle">@RKMarlowLive</p>
  </article>
  <article class="quote-card col-5 row-1">
    <p class="quote-text">Sis, your<br><span class="hl">hormones</span><br>are out of<br>whack -<br>that's why<br>the weight<br><span class="hl">&nbsp;won't budge!&nbsp;</span></p>
    <p class="handle">@RKMarlowLive</p>
  </article>

  <article class="quote-card col-1 row-2">
    <p class="quote-text">Frustrated with<br><span class="hl">belly fat that won't</span><br>budge? I've got the<br>solution that<br>finally worked for<br>me-<span class="hl">no crazy diets</span><br>required</p>
    <p class="handle">@RKMarlowLive</p>
  </article>
  <article class="quote-card col-2 row-2">
    <p class="quote-text">That<br><span class="hl">stubborn belly fat</span><br>isn't your fault -<br>here's what<br>no one<br><span class="hl">&nbsp;&nbsp;tells you&nbsp;&nbsp;</span></p>
    <p class="handle">@RKMarlowLive</p>
  </article>
  <article class="quote-card col-3 row-2">
    <p class="quote-text"><span class="hl">You've been lied to</span><br>- 'just eat less and<br>exercise more'<br>doesn't work in<br><span class="hl">&nbsp;&nbsp;menopause&nbsp;&nbsp;</span></p>
    <p class="handle">@RKMarlowLive</p>
  </article>
  <article class="quote-card col-4 row-2">
    <p class="quote-text">A natural way<br>to <span class="hl">boost GLP-1</span><br>- no injections,<br>no side effects,<br>just real<br>results. Here's<br><span class="hl">&nbsp;how it works&nbsp;</span></p>
    <p class="handle">@RKMarlowLive</p>
  </article>
  <article class="quote-card col-5 row-2">
    <p class="quote-text"><span class="hl">GLP-1:</span> the magic<br>behind the weight<br>loss drugs. But here's<br>the secret - you can<br>boost it naturally<br>without a<br><span class="hl">&nbsp;prescription!&nbsp;</span></p>
    <p class="handle">@RKMarlowLive</p>
  </article>
</main>
</body>
</html>
```